Quenderil - Still Grace Cosmetics

Please design a logo and business cards for new food supplements, cosmetics and herbal fixatives. The products are produced ecologically and biologically in the South Tyrol and Trentino alps. The products are pure and noble. Quenderil = pure vitality Colors Background: dark or black matt (soft touch) Logodesign: powerful, elegant, violet with glossy foil The logo and design should convey warmth, passion and the 6th sense, you should get the impression that you can smell the herbal odor , Logo and business cards for new food supplements, cosmetics and herbal fixatives. The products are produced ecologically and biologically in the South Tyrol and Trentino alps. The products are pure and noble. Quenderil = pure vitality Colors Background: dark or black matt (softtouch) Logodesign: powerful elegant violet with glossy foil The logo and design is meant to convey warmth, passion and the 6th sense, you should get the impression that you can smell the herbal perfume.

Target Market(s)

Food, food supplements, vitality, health

Contact Information for Business Card

Please provide an elegant darf design that is puristic, but has a very good logo design
Elegantes dunkles design, puristisch

Logo Text

Quenderil - still Grace

Colors
6b449b

Requirements
Must have
• SVG Files Alpha channel for foil embossing High-quality design
Nice to have
• Pure elegance
Should not have
• to colorful colors

```html
<!DOCTYPE html>
<html lang="en">
<head>
<meta charset="utf-8">
<title>Quenderil – Business Card</title>
<link rel="stylesheet" href="https://fonts.googleapis.com/css2?family=Montserrat:wght@400;500&display=swap">
<style>
  :root {
    --stage: #1c1c1e;
    --card: #0d0d0f;
    --violet: #6b449b;
    --violet-light: #7d5cb6;
    --ink: #e6e6ea;
  }
  * { margin: 0; padding: 0; box-sizing: border-box; }
  html, body { width: 1200px; height: 873px; overflow: hidden; }
  body {
    background: var(--stage);
    font-family: "Montserrat", sans-serif;
    display: flex;
    flex-direction: column;
    align-items: center;
    justify-content: center;
    gap: 56px;
  }
  .card {
    position: relative;
    width: 560px;
    height: 320px;
    background: var(--card);
    border-radius: 18px;
    box-shadow: 0 14px 40px rgba(0,0,0,0.55);
  }
  .brand-name {
    position: absolute;
    font-weight: 500;
    color: var(--violet-light);
    letter-spacing: 0.02em;
    white-space: nowrap;
  }
  .card-front .brand-name {
    left: 44px;
    bottom: 50px;
    font-size: 46px;
  }
  .card-back .brand-name {
    left: 40px;
    top: 100px;
    font-size: 48px;
  }
  .contact {
    position: absolute;
    right: 28px;
    top: 150px;
    text-align: right;
    color: var(--ink);
  }
  .contact-name { font-size: 17px; font-weight: 400; letter-spacing: 0.03em; margin-right: 26px; }
  .contact-role { font-size: 12px; color: var(--violet-light); letter-spacing: 0.02em; margin: 2px 26px 10px 0; }
  .contact-line {
    display: flex;
    justify-content: flex-end;
    align-items: center;
    gap: 8px;
    font-size: 13px;
    line-height: 22px;
    letter-spacing: 0.02em;
  }
  .contact-line .icon { width: 16px; height: 16px; flex: none; }
  .contact-line .icon-gap { width: 16px; flex: none; }
</style>
</head>
<body>
  <section class="card card-front" aria-label="Card front">
    <span class="brand-name">Quenderil</span>
  </section>

  <section class="card card-back" aria-label="Card back">
    <span class="brand-name">Quenderil</span>
    <div class="contact">
      <p class="contact-name">Marlon Eberle</p>
      <p class="contact-role">Managing Director</p>
      <p class="contact-line">0492 517 068
        <svg class="icon" viewBox="0 0 16 16" aria-hidden="true"><path fill="#7d5cb6" d="M4.2 1.5l2 2.6-1.2 1.6c.8 1.9 2.4 3.5 4.3 4.3l1.6-1.2 2.6 2-.9 2.2c-.3.6-1 .9-1.6.7C6.3 12.4 3.6 9.7 2.3 5.1c-.2-.6.1-1.3.7-1.6z"/></svg>
      </p>
      <p class="contact-line">quenderilmail.com
        <svg class="icon" viewBox="0 0 16 16" aria-hidden="true"><rect x="1.5" y="3.5" width="13" height="9" rx="1" fill="#7d5cb6"/><path d="M2 4.2l6 4.6 6-4.6" fill="none" stroke="#0d0d0f" stroke-width="1.2"/></svg>
      </p>
      <p class="contact-line">hello@quenderilmail.com.au
        <svg class="icon" viewBox="0 0 16 16" aria-hidden="true"><circle cx="8" cy="8" r="6.5" fill="#7d5cb6"/><g fill="none" stroke="#0d0d0f" stroke-width="1"><ellipse cx="8" cy="8" rx="2.8" ry="6.5"/><path d="M1.5 8h13M2.5 5h11M2.5 11h11"/></g></svg>
      </p>
      <p class="contact-line">quenderil.com.au<span class="icon-gap"></span></p>
    </div>
  </section>
</body>
</html>
```